QBRF Business Card

I have a logo, which was designed by pixel harbor.

Front of card
QBRF Logo
Dorian Felsby
CEO-Trainer-Assessor
0419557308
www.qbrf-example.com.au
Training Address: Warehouse 14 Quarry Rd Brellhaven Tas
Head Office: 62 Linfield Avenue Brellhaven Tas 7151

Back of card
QBRF Logo
QBRF provides Nationally accredited training in:
HLTAID001 Provide cardiopulmonary resuscitation
HLTAID002 Provide basic emergency life support
HLTAID003 Provide First Aid
HLTAID007 Provide advanced resuscitation
MSMWHS217 Gas test atmospheres
RIIWHS202D Enter and work in confined spaces
RIIWHS204D Work Safely at Heights
UETTDRRF04B Perform Tower Rescue
UETTDRRF06B Perform rescue from a live LV panel

```html
<!DOCTYPE html>
<html lang="en">
<head>
<meta charset="utf-8">
<title>QBRF Business Card</title>
<link rel="stylesheet" href="https://fonts.googleapis.com/css2?family=Arimo:wght@400;700&display=swap">
<style>
  :root {
    --board: #cccccc;
    --card-dark: #333333;
    --card-light: #ffffff;
    --ink-light: #f2f2f2;
    --ink-blue: #1a5ea8;
    --brand: #2b7fd0;
    --mark-dark: #4a4a4a;
    --mark-light: #eeeeee;
  }
  * { margin: 0; padding: 0; box-sizing: border-box; }
  html, body { width: 1200px; height: 845px; overflow: hidden; }
  body {
    background: var(--board);
    font-family: "Arimo", Arial, sans-serif;
    position: relative;
  }
  .card {
    position: absolute;
    width: 424px;
    height: 235px;
    overflow: hidden;
    box-shadow: 3px 4px 6px rgba(0,0,0,0.35);
  }
  .card--dark { background: var(--card-dark); color: var(--ink-light); }
  .card--light { background: var(--card-light); color: var(--ink-blue); }
  .card--front-dark { left: 130px; top: 158px; }
  .card--back-dark { left: 640px; top: 158px; }
  .card--front-light { left: 130px; top: 454px; }
  .card--back-light { left: 640px; top: 454px; }

  .bg-mark {
    position: absolute;
    right: -4px;
    top: 122px;
    font-size: 80px;
    font-weight: 700;
    line-height: 1;
    letter-spacing: 2px;
  }
  .card--dark .bg-mark { color: var(--mark-dark); }
  .card--light .bg-mark { color: var(--mark-light); }

  .brand {
    position: absolute;
    display: flex;
    align-items: center;
    gap: 6px;
    color: var(--brand);
    font-weight: 700;
  }
  .brand__dot {
    border: 2px solid var(--brand);
    border-radius: 50%;
  }
  .brand--front { left: 0; right: 0; top: 16px; justify-content: center; font-size: 22px; }
  .brand--front .brand__dot { width: 34px; height: 34px; }
  .brand--back { left: 28px; top: 14px; font-size: 16px; }
  .brand--back .brand__dot { width: 26px; height: 26px; }

  .contact {
    position: absolute;
    left: 0; right: 0;
    top: 95px;
    text-align: center;
    line-height: 20px;
  }
  .contact__name { font-size: 16px; }
  .contact__title { font-size: 14px; font-weight: 700; }
  .contact__phone, .contact__web { font-size: 15px; }

  .addresses {
    position: absolute;
    top: 180px;
    left: 0;
    font-size: 10.5px;
    line-height: 16px;
    border-collapse: collapse;
  }
  .addresses th {
    width: 166px;
    text-align: right;
    font-weight: 400;
    padding-right: 11px;
    white-space: nowrap;
  }
  .addresses td { text-align: left; white-space: nowrap; }

  .courses {
    position: absolute;
    left: 31px;
    top: 57px;
  }
  .courses__intro { font-size: 12.5px; margin-bottom: 10px; }
  .courses__list { list-style: none; font-size: 11.2px; line-height: 14.4px; }
</style>
</head>
<body>

  <section class="card card--dark card--front-dark">
    <div class="bg-mark" aria-hidden="true">QBRF</div>
    <div class="brand brand--front"><span class="brand__dot"></span>QBRF</div>
    <div class="contact">
      <p class="contact__name">Dorian Felsby</p>
      <p class="contact__title">CEO-Trainer-Assessor</p>
      <p class="contact__phone">0419557308</p>
      <p class="contact__web">www.qbrf-example.com.au</p>
    </div>
    <table class="addresses">
      <tr><th>Training Address:</th><td>Warehouse 14 Quarry Rd Brellhaven Tas</td></tr>
      <tr><th>Head Office:</th><td>62 Linfield Avenue Brellhaven Tas 7151</td></tr>
    </table>
  </section>

  <section class="card card--dark card--back-dark">
    <div class="bg-mark" aria-hidden="true">QBRF</div>
    <div class="brand brand--back"><span class="brand__dot"></span>QBRF</div>
    <div class="courses">
      <p class="courses__intro">QBRF provides Nationally accredited training in:</p>
      <ul class="courses__list">
        <li>HLTAID001 Provide cardiopulmonary resuscitation</li>
        <li>HLTAID002 Provide basic emergency life support</li>
        <li>HLTAID003 Provide First Aid</li>
        <li>HLTAID007 Provide advanced resuscitation</li>
        <li>MSMWHS217 Gas test atmospheres</li>
        <li>RIIWHS202D Enter and work in confined spaces</li>
        <li>RIIWHS204D Work Safely at Heights</li>
        <li>UETTDRRF04B Perform Tower Rescue</li>
        <li>UETTDRRF06B Perform rescue from a live LV panel</li>
      </ul>
    </div>
  </section>

  <section class="card card--light card--front-light">
    <div class="bg-mark" aria-hidden="true">QBRF</div>
    <div class="brand brand--front"><span class="brand__dot"></span>QBRF</div>
    <div class="contact">
      <p class="contact__name">Dorian Felsby</p>
      <p class="contact__title">CEO-Trainer-Assessor</p>
      <p class="contact__phone">0419557308</p>
      <p class="contact__web">www.qbrf-example.com.au</p>
    </div>
    <table class="addresses">
      <tr><th>Training Address:</th><td>Warehouse 14 Quarry Rd Brellhaven Tas</td></tr>
      <tr><th>Head Office:</th><td>62 Linfield Avenue Brellhaven Tas 7151</td></tr>
    </table>
  </section>

  <section class="card card--light card--back-light">
    <div class="bg-mark" aria-hidden="true">QBRF</div>
    <div class="brand brand--back"><span class="brand__dot"></span>QBRF</div>
    <div class="courses">
      <p class="courses__intro">QBRF provides Nationally accredited training in:</p>
      <ul class="courses__list">
        <li>HLTAID001 Provide cardiopulmonary resuscitation</li>
        <li>HLTAID002 Provide basic emergency life support</li>
        <li>HLTAID003 Provide First Aid</li>
        <li>HLTAID007 Provide advanced resuscitation</li>
        <li>MSMWHS217 Gas test atmospheres</li>
        <li>RIIWHS202D Enter and work in confined spaces</li>
        <li>RIIWHS204D Work Safely at Heights</li>
        <li>UETTDRRF04B Perform Tower Rescue</li>
        <li>UETTDRRF06B Perform rescue from a live LV panel</li>
      </ul>
    </div>
  </section>

</body>
</html>
```